Podcast Cover Art for Inspiring Fun Show

Title: The Dave R Hour

I am looking for a simple design that includes the following:

1. Picture of me (the one I attached with the background removed) on a simple background (please refer to attachments for ideas).
2. The title done in professional lettering that is easy to read and stands out on the background

Please see attached pictures for:

1) Other podcast art I like
2) Backgrounds that I like
3) A picture of me (please edit out the background)

Target Market(s)

Anyone into personal-development, inspiring content and motivational stories.

Font styles to use
Sans Serif

Colors

Designer to choose colors to be used in the design.

Requirements
Must have
• - Title "The Dave R Hour" in professional lettering that is large and very easy to read
• - Picture of me on the background

```html
<!DOCTYPE html>
<html lang="en">
<head>
<meta charset="utf-8">
<title>The Dave R Hour – Cover Options</title>
<link rel="stylesheet" href="https://fonts.googleapis.com/css2?family=Fira+Sans+Condensed:wght@800&display=swap">
<style>
  :root {
    --stage: #111111;
    --wall-light: #fbdc1e;
    --wall-mid: #f4cf0c;
    --wall-deep: #e6bc00;
    --photo-top: #2a2422;
    --photo-mid: #d9a88e;
    --photo-low: #e3b79f;
    --photo-base: #3a3b40;
    --title-light: #ffffff;
    --title-dark: #0b0b0b;
  }
  * { margin: 0; padding: 0; box-sizing: border-box; }
  html, body {
    width: 1200px;
    height: 640px;
    overflow: hidden;
    background: var(--stage);
  }
  .stage {
    position: relative;
    width: 1200px;
    height: 640px;
  }
  .cover {
    position: absolute;
    top: 82px;
    width: 480px;
    height: 480px;
    overflow: hidden;
  }
  .cover--light-title { left: 99px; }
  .cover--dark-title { left: 622px; }
  .cover__wall {
    position: absolute;
    inset: 0;
    background:
      repeating-linear-gradient(90deg,
        rgba(0,0,0,0) 0 40px,
        rgba(190,140,0,0.35) 40px 42px),
      radial-gradient(circle at 35% 40%, var(--wall-light), var(--wall-mid) 60%, var(--wall-deep));
  }
  .cover__host-photo {
    position: absolute;
    left: 348px;
    right: 0;
    top: 54px;
    bottom: 0;
    background: linear-gradient(180deg,
      var(--photo-top) 0%,
      var(--photo-mid) 22%,
      var(--photo-low) 70%,
      var(--photo-base) 100%);
  }
  .cover__title {
    position: absolute;
    left: 8px;
    top: 112px;
    width: 330px;
    text-align: center;
    font-family: "Fira Sans Condensed", "Arial Narrow", sans-serif;
    font-weight: 800;
    text-transform: uppercase;
    letter-spacing: 0;
  }
  .cover__title span { display: block; white-space: nowrap; }
  .cover__title .line-small { font-size: 96px; line-height: 0.82; }
  .cover__title .line-large { font-size: 112px; line-height: 0.86; }
  .cover--light-title .cover__title {
    color: var(--title-light);
    text-shadow: 2px 3px 6px rgba(0,0,0,0.3);
  }
  .cover--dark-title .cover__title { color: var(--title-dark); }
</style>
</head>
<body>
<main class="stage">

  <section class="cover cover--light-title">
    <div class="cover__wall" role="img" aria-label="Yellow painted wooden plank wall"></div>
    <div class="cover__host-photo" role="img" aria-label="Photo of the host, cropped at the right edge"></div>
    <h1 class="cover__title">
      <span class="line-small">The</span>
      <span class="line-large">Dave R</span>
      <span class="line-large">Hour</span>
    </h1>
  </section>

  <section class="cover cover--dark-title">
    <div class="cover__wall" role="img" aria-label="Yellow painted wooden plank wall"></div>
    <div class="cover__host-photo" role="img" aria-label="Photo of the host, cropped at the right edge"></div>
    <h1 class="cover__title">
      <span class="line-small">The</span>
      <span class="line-large">Dave R</span>
      <span class="line-large">Hour</span>
    </h1>
  </section>

</main>
</body>
</html>
```